Visitenkarten-Design für Immobilienmakler
Zielgruppe
Wir sind ein Immobilienmakler.
Aufgabenstellung
Wicht wäre das es im Druckformat geliefert wird, welches von www.Kravendo.de geliefert wird. Ich habe alle möglichen Logo Varianten angehangen.

```html
<!DOCTYPE html>
<html lang="en">
<head>
<meta charset="utf-8">
<title>Marlow Estates – Business Card</title>
<link href="https://fonts.googleapis.com/css2?family=Open+Sans:wght@400;700&family=Roboto+Condensed:wght@400;700&display=swap" rel="stylesheet">
<style>
  :root {
    --stage: #1c1c1c;
    --card: #252525;
    --card-edge: #2e2e2e;
    --white: #ffffff;
    --muted: #cfcfcf;
    --accent: #f7941d;
    --accent-deep: #f26722;
    --pattern-dark: #202020;
    --pattern-light: #3a3a3a;
  }
  * { margin: 0; padding: 0; box-sizing: border-box; }
  html, body {
    width: 1200px; height: 901px; overflow: hidden;
    background: var(--stage);
    font-family: "Open Sans", sans-serif;
  }
  .stage {
    width: 1200px; height: 901px;
    display: flex; align-items: center; justify-content: center; gap: 60px;
  }
  .card {
    position: relative;
    width: 510px; height: 330px;
    background: var(--card);
    border: 1px solid var(--card-edge);
    border-radius: 4px;
    overflow: hidden;
    box-shadow: 0 20px 40px rgba(0,0,0,.5);
  }
  .brand {
    display: flex; align-items: center; gap: 8px;
    font-family: "Open Sans", sans-serif;
    font-weight: 700; color: var(--white);
    letter-spacing: 2px;
  }
  .brand-mark { width: 14px; height: 14px; background: var(--accent); }
  .card-front .brand {
    position: absolute; top: 92px; left: 0; right: 0;
    justify-content: center; font-size: 30px;
  }
  .holder {
    position: absolute; left: 48px; bottom: 74px; text-align: right;
  }
  .holder-name {
    font-family: "Roboto Condensed", sans-serif;
    font-weight: 700; font-size: 26px; color: var(--white);
  }
  .holder-role {
    font-family: "Roboto Condensed", sans-serif;
    font-size: 14px; color: var(--muted);
  }
  .divider {
    position: absolute; left: 248px; bottom: 70px;
    width: 2px; height: 62px; background: var(--accent);
  }
  .contacts {
    position: absolute; left: 264px; bottom: 70px;
    list-style: none; font-size: 13px; color: var(--white);
  }
  .contacts li { display: flex; align-items: center; gap: 8px; line-height: 21px; }
  .contacts svg { width: 12px; height: 12px; fill: var(--accent); flex: none; }
  .pattern-field {
    position: absolute; inset: 0;
    background: linear-gradient(120deg, var(--pattern-light) 0%, var(--pattern-dark) 70%);
  }
  .card-back .brand {
    position: absolute; right: 40px; bottom: 120px; font-size: 22px;
  }
</style>
</head>
<body>
<main class="stage">
  <section class="card card-front" aria-label="Card front">
    <div class="brand"><span class="brand-mark"></span>MARLOW ESTATES</div>
    <div class="holder">
      <p class="holder-name">Daniel Hartley</p>
      <p class="holder-role">Owner-Director</p>
    </div>
    <span class="divider"></span>
    <ul class="contacts">
      <li><svg viewBox="0 0 24 24"><path d="M6.6 10.8a15 15 0 0 0 6.6 6.6l2.2-2.2c.3-.3.7-.4 1-.2 1.1.4 2.3.6 3.6.6.6 0 1 .4 1 1V20c0 .6-.4 1-1 1A17 17 0 0 1 3 4c0-.6.4-1 1-1h3.5c.6 0 1 .4 1 1 0 1.3.2 2.5.6 3.6.1.3 0 .7-.2 1z"/></svg>0790 000 418</li>
      <li><svg viewBox="0 0 24 24"><path d="M2 5h20v14H2zm2 2v.5l8 5 8-5V7z"/></svg>hello@marlowestates.uk</li>
      <li><svg viewBox="0 0 24 24"><path d="M12 2a10 10 0 1 0 0 20 10 10 0 0 0 0-20zm0 2c.9 1.2 1.6 3 1.9 5h-3.8c.3-2 1-3.8 1.9-5zM4.3 14a8 8 0 0 1 0-4h3.9a16 16 0 0 0 0 4zm5.8 0a14 14 0 0 1 0-4h3.8a14 14 0 0 1 0 4zm5.7 0a16 16 0 0 0 0-4h3.9a8 8 0 0 1 0 4zM12 20c-.9-1.2-1.6-3-1.9-5h3.8c-.3 2-1 3.8-1.9 5z"/></svg>marlowestates.co.uk</li>
    </ul>
  </section>

  <section class="card card-back" aria-label="Card back">
    <div class="pattern-field" role="img" aria-label="Repeating grey key pattern across the card back"></div>
    <div class="brand"><span class="brand-mark"></span>MARLOW ESTATES</div>
  </section>
</main>
</body>
</html>
```